Financial PR company Homepage and Inner Page design

Please design a web homepage and innerpage for OVIN Public Relations.
OVIN Public Relations is a Financial PR company targeting Shenzhen Qian Special Economical Zone.
Note:
1. Menu includes ( Please specialize in Chinese and we want to see the Chinese fonts)
关于我们/服务板块/专业优势/合作伙伴/前海商圈/公司新闻/加盟我们/联系我们

2. Please refer to world class PR Business company and contribute your idea on website design and color themes.

3. We have attached the Logo for reference.

4. Anytime use picture for reference, please select asian business people pictures.

Cheers,

HI Designers, Thanks for the design submission. Here is our client feedback: 1. Adopt one screen design. 2. Use amiable Asia Business woman pictures. 3. Use contrastive color theme for the design. Cheers, Kip From TW

```html
<!DOCTYPE html>
<html lang="zh-CN">
<head>
<meta charset="utf-8">
<title>OVIN PR – Financial Public Relations</title>
<link href="https://fonts.googleapis.com/css2?family=Open+Sans:wght@400;600;700&family=Oswald:wght@400;500&family=Noto+Sans+SC:wght@500;700&display=swap" rel="stylesheet">
<style>
:root{
  --blue:#2aa3df;
  --blue-light:#5cc3ee;
  --navy:#1d3b57;
  --navy-deep:#16314a;
  --ink:#333b44;
  --muted:#6b737b;
  --grey-bg:#eef0f2;
  --footer:#2b2f33;
  --footer-bar:#3fb0e6;
  --white:#fff;
}
*{box-sizing:border-box;margin:0;padding:0}
html,body{width:1200px;height:2767px;overflow:hidden}
body{font-family:"Open Sans",Arial,sans-serif;color:var(--ink);background:var(--white);font-size:15px;line-height:1.55}
.wrap{width:1060px;margin:0 auto;position:relative}

/* header */
.site-header{height:97px;background:var(--white);position:relative}
.site-header .wrap{height:97px;display:flex;align-items:center;justify-content:space-between}
.brand{display:flex;align-items:center;gap:14px}
.brand-mark{width:38px;height:38px;border-radius:50%;background:var(--blue)}
.brand-name{font-size:34px;font-weight:700;color:var(--blue);letter-spacing:1px;line-height:1}
.brand-tag{font-size:12px;color:var(--muted);margin-top:4px}
.header-contact{display:flex;gap:14px;margin-top:22px}
.pill{display:flex;align-items:center;gap:8px;border:1px solid #d9dde1;border-radius:20px;padding:6px 16px 6px 8px;font-size:16px;font-weight:600;color:var(--navy)}
.pill .dot{width:26px;height:26px;border-radius:50%;background:var(--blue);display:flex;align-items:center;justify-content:center}
.flags{position:absolute;right:70px;top:0;display:flex;gap:6px}
.flag{width:30px;height:20px}
.flag.red{background:#d8312c}
.flag.blue{background:#25407a}

/* nav */
.main-nav{height:48px;background:var(--blue)}
.main-nav ul{list-style:none;display:flex;height:48px}
.main-nav li{height:48px;display:flex;align-items:center;padding:0 26px;color:var(--white);font-family:"Noto Sans SC","Open Sans",sans-serif;font-size:15px;font-weight:500;letter-spacing:1px;border-right:1px solid rgba(255,255,255,.25)}
.main-nav li.home{background:var(--navy);padding:0 16px}

/* hero */
.hero{height:477px;position:relative;background:
  radial-gradient(ellipse 260px 300px at 12% 55%,#e9d8c8 0%,rgba(233,216,200,0) 70%),
  radial-gradient(ellipse 240px 280px at 45% 50%,#7f9cbc 0%,rgba(127,156,188,0) 70%),
  radial-gradient(ellipse 220px 260px at 80% 40%,#e6d2c2 0%,rgba(230,210,194,0) 70%),
  linear-gradient(100deg,#f3f5f7 0%,#d7e1ea 35%,#b9cadb 55%,#e4e9ee 80%,#f6f7f8 100%)}
.hero-caption{position:absolute;left:655px;top:250px}
.hero-line{font-family:"Oswald",sans-serif;color:var(--white);font-size:36px;line-height:1;padding:10px 16px;display:inline-block}
.hero-line.one{background:var(--blue)}
.hero-line.two{background:var(--navy);margin-top:6px}
.btn{display:inline-block;background:var(--navy);color:var(--white);font-size:14px;font-weight:600;padding:8px 22px;border-radius:3px}
.hero .btn{background:var(--blue);margin-top:12px;margin-left:30px}

/* sections */
.section-title{font-size:34px;font-weight:400;text-align:center;color:var(--ink);letter-spacing:1px}
.section-title span{color:var(--blue)}
.title-rule{width:90px;height:2px;background:var(--blue);margin:10px auto 22px}

.welcome{height:295px;padding-top:40px;text-align:center}
.welcome p{font-size:14px;color:var(--muted);width:920px;margin:0 auto}
.welcome .btn{margin-top:22px}

.services{height:380px;background:linear-gradient(180deg,var(--navy) 0%,var(--navy-deep) 100%);padding-top:40px;color:var(--white);text-align:center}
.services .section-title{color:var(--white)}
.services .lead{font-size:14px;opacity:.85}
.service-list{display:flex;justify-content:center;gap:60px;margin-top:32px}
.service{width:150px;text-align:center}
.service-icon{width:110px;height:110px;border-radius:50%;border:4px solid var(--white);margin:0 auto 14px;display:flex;align-items:center;justify-content:center}
.service h3{font-size:14px;font-weight:700;line-height:1.3}

.advantage{height:416px;background:var(--grey-bg);padding-top:30px}
.advantage-card{background:var(--white);height:360px;padding:28px 30px;display:flex;gap:30px}
.advantage-text{flex:1}
.advantage-card .section-title{text-align:left;font-size:30px;font-weight:700}
.advantage-card .title-rule{margin:8px 0 18px}
.advantage h4{color:var(--blue);font-size:15px;font-weight:600;margin-bottom:6px}
.advantage p{font-size:13px;color:var(--muted)}
.ticks{list-style:none;margin-top:12px}
.ticks li{font-size:13px;color:var(--muted);display:flex;gap:10px;align-items:center;margin-bottom:6px}
.advantage-art{width:420px;background:
  radial-gradient(ellipse 140px 90px at 50% 45%,#f4f7fb 0%,rgba(244,247,251,0) 75%),
  linear-gradient(135deg,#1f5fa8 0%,#3f8fd6 45%,#8cc4ee 100%)}

.join{height:242px;display:flex}
.join-photo{width:380px;background:
  radial-gradient(ellipse 90px 120px at 30% 55%,#2c3e55 0%,rgba(44,62,85,0) 75%),
  radial-gradient(ellipse 90px 120px at 72% 55%,#34495f 0%,rgba(52,73,95,0) 75%),
  linear-gradient(120deg,#cfd9e3 0%,#eef2f6 50%,#bccbd9 100%)}
.join-body{flex:1;background:var(--blue-light);padding:30px 40px;color:var(--navy-deep)}
.join-body h2{font-size:34px;font-weight:700;letter-spacing:1px}
.join-body p{font-size:13px;margin:8px 0 16px;max-width:720px}
.join-body .btn{display:inline-flex;align-items:center;gap:8px}

.partners{height:121px;display:flex;align-items:center;justify-content:center;gap:48px}
.partner{font-size:26px;font-weight:700;color:#2f3338}
.arrow{color:#999;font-size:28px}

.news{height:399px;background:var(--grey-bg);padding-top:30px}
.news-list{display:flex;gap:40px}
.news-item{flex:1;display:flex;background:var(--white);height:250px}
.news-photo{width:230px}
.news-photo.office{background:
  radial-gradient(ellipse 80px 110px at 45% 45%,#e7cdb9 0%,rgba(231,205,185,0) 75%),
  linear-gradient(160deg,#f2f0ec 0%,#d9dee4 60%,#b7c3cf 100%)}
.news-photo.portrait{background:
  radial-gradient(ellipse 90px 70px at 50% 80%,#2b3644 0%,rgba(43,54,68,0) 80%),
  radial-gradient(ellipse 60px 70px at 50% 35%,#e2c3a8 0%,rgba(226,195,168,0) 80%),
  linear-gradient(180deg,#f7f8f9 0%,#e6eaee 100%)}
.news-body{flex:1;padding:14px 18px}
.news-body h3{color:var(--blue);font-size:17px;font-weight:600}
.news-date{font-size:13px;font-weight:600;margin:6px 0;display:flex;gap:8px;align-items:center}
.news-date i{width:24px;height:24px;background:#d9dde1;display:inline-block}
.news-body p{font-size:12px;color:var(--muted);line-height:1.5}
.news-body .more{font-size:13px;font-weight:700;margin-top:6px;display:block}

.site-footer{height:241px;background:var(--footer);color:#cfd3d6;padding-top:24px}
.site-footer .wrap{display:flex;gap:60px}
.site-footer h5{color:var(--white);font-size:14px;font-weight:600;margin-bottom:10px}
.links{list-style:none;font-size:12px;line-height:1.75;width:160px}
.signup{width:230px;font-size:12px}
.signup .field{background:var(--white);color:#888;padding:5px 8px;margin:10px 0 8px;font-size:11px}
.signup .btn{background:var(--blue);font-size:11px;padding:4px 12px}
.contact{font-size:12px;line-height:1.7;flex:1;display:flex;gap:24px}
.contact-lines div{display:flex;gap:8px;align-items:flex-start;margin-bottom:6px}
.contact-lines i{width:16px;height:16px;border-radius:50%;background:var(--blue);flex:none;margin-top:2px}
.map{width:250px;height:140px;background:linear-gradient(135deg,#ece8dc 0%,#dfe4e0 50%,#c4d6e6 100%);margin-top:30px}

.footer-bar{height:51px;background:var(--footer-bar);color:var(--white);font-size:12px}
.footer-bar .wrap{height:51px;display:flex;align-items:center;justify-content:space-between}
.follow{display:flex;align-items:center;gap:8px;font-weight:600}
.follow i{width:20px;height:20px;background:rgba(255,255,255,.85);display:inline-block}
</style>
</head>
<body>

<header class="site-header">
  <div class="flags">
    <div class="flag red" role="img" aria-label="Chinese language flag"></div>
    <div class="flag blue" role="img" aria-label="English language flag"></div>
  </div>
  <div class="wrap">
    <div class="brand">
      <div class="brand-mark"></div>
      <div>
        <div class="brand-name">OVIN PR</div>
        <div class="brand-tag">Financial Public Relations</div>
      </div>
    </div>
    <div class="header-contact">
      <div class="pill"><span class="dot"><svg width="14" height="14" viewBox="0 0 24 24"><path fill="#fff" d="M6.6 10.8a15 15 0 006.6 6.6l2.2-2.2c.3-.3.7-.4 1-.2 1.1.4 2.3.6 3.6.6.6 0 1 .4 1 1V20c0 .6-.4 1-1 1A17 17 0 013 4c0-.6.4-1 1-1h3.5c.6 0 1 .4 1 1 0 1.3.2 2.5.6 3.6.1.3 0 .7-.2 1z"/></svg></span>555-018-2046</div>
      <div class="pill"><span class="dot"><svg width="14" height="14" viewBox="0 0 24 24"><path fill="#fff" d="M3 5h18v14H3z"/><path d="M3 5l9 7 9-7" stroke="#2aa3df" stroke-width="2" fill="none"/></svg></span>info@ovinpr.com</div>
    </div>
  </div>
</header>

<nav class="main-nav">
  <ul class="wrap">
    <li class="home"><svg width="18" height="16" viewBox="0 0 24 22"><path fill="#fff" d="M12 2L1 12h3v9h6v-6h4v6h6v-9h3z"/></svg></li>
    <li>关于我们</li><li>服务板块</li><li>专业优势</li><li>前海商圈</li><li>公司新闻</li><li>加盟我们</li><li>联系我们</li>
  </ul>
</nav>

<section class="hero" role="img" aria-label="Photo of smiling Asian businesswomen and colleagues meeting around a laptop in a bright office">
  <div class="hero-caption">
    <div class="hero-line one">OUR COMPANY IS A FINANCIAL</div><br>
    <div class="hero-line two">PUBLIC RELATION COMPANY</div><br>
    <span class="btn">LEARN MORE ›</span>
  </div>
</section>

<section class="welcome">
  <h2 class="section-title">WELCOME TO <span>OVIN PR</span></h2>
  <div class="title-rule"></div>
  <p>Lorem ipsum dolor sit amet, consectetuer adipiscing elit, sed diam nonummy nibh euismod tincidunt ut laoreet dolore magna aliquam erat volutpat. Ut wisi enim ad minim veniam, quis nostrud exerci tation ullamcorper suscipit lobortis nisl ut aliquip ex ea commodo consequat. Duis autem vel eum iriure dolor in hendrerit in vulputate velit esse molestie consequat, vel illum dolore eu feugiat nulla facilisis at vero eros et accumsan et iusto odio dignissim qui blandit praesent luptatum zzril delenit augue duis dolore te feugait nulla facilisi.</p>
  <span class="btn">Read More</span>
</section>

<section class="services">
  <h2 class="section-title">SERVICE <span>SECTOR</span></h2>
  <div class="title-rule"></div>
  <p class="lead">Ut wisi enim ad minim veniam, quis nostrud exerci tation ullamcorper suscipit lobortis nisl ut aliquip.</p>
  <div class="service-list">
    <div class="service">
      <div class="service-icon"><svg width="54" height="54" viewBox="0 0 48 48" fill="#fff"><path d="M24 4L4 14v4h40v-4z"/><rect x="8" y="20" width="5" height="16"/><rect x="17" y="20" width="5" height="16"/><rect x="26" y="20" width="5" height="16"/><rect x="35" y="20" width="5" height="16"/><rect x="4" y="38" width="40" height="5"/></svg></div>
      <h3>MEDIA &amp; PUBLIC<br>RELATIONS</h3>
    </div>
    <div class="service">
      <div class="service-icon"><svg width="54" height="54" viewBox="0 0 48 48" fill="#fff"><circle cx="16" cy="16" r="7"/><circle cx="32" cy="16" r="7"/><path d="M2 40c0-8 6-14 14-14s14 6 14 14z"/><path d="M22 40c0-8 4-14 10-14 8 0 14 6 14 14z"/></svg></div>
      <h3>GOVERNMENT<br>RELATIONS</h3>
    </div>
    <div class="service">
      <div class="service-icon"><svg width="54" height="54" viewBox="0 0 48 48"><rect x="6" y="8" width="30" height="26" fill="none" stroke="#fff" stroke-width="3"/><circle cx="30" cy="30" r="9" fill="none" stroke="#fff" stroke-width="4"/><path d="M37 37l8 8" stroke="#fff" stroke-width="5"/></svg></div>
      <h3>PUBLIC RELATIONS<br>RESEARCH</h3>
    </div>
    <div class="service">
      <div class="service-icon"><svg width="54" height="54" viewBox="0 0 48 48"><rect x="6" y="8" width="36" height="26" fill="none" stroke="#fff" stroke-width="3"/><path d="M20 15v12l10-6z" fill="#fff"/><path d="M16 42h16M24 34v8" stroke="#fff" stroke-width="3"/></svg></div>
      <h3>ADVOCACY<br>ADVERTISING</h3>
    </div>
    <div class="service">
      <div class="service-icon"><svg width="54" height="54" viewBox="0 0 48 48" fill="none" stroke="#fff" stroke-width="3"><circle cx="24" cy="24" r="18"/><circle cx="24" cy="24" r="11"/><circle cx="24" cy="24" r="4" fill="#fff"/><path d="M24 24l16-16"/></svg></div>
      <h3>PR &amp; MARKETING<br>STRATEGIES</h3>
    </div>
  </div>
</section>

<section class="advantage">
  <div class="wrap advantage-card">
    <div class="advantage-text">
      <h2 class="section-title">PROFESSIONAL <span>ADVANTAGE</span></h2>
      <div class="title-rule"></div>
      <h4>Accumsan Et Iusto Odio Dignissim Qui Blandit Praesent</h4>
      <p>Lorem ipsum dolor sit amet, consectetuer adipiscing elit, sed diam nonummy nibh euismod tincidunt ut laoreet dolore magna aliquam erat volutpat. Ut wisi enim ad minim veniam, exerci tation.</p>
      <ul class="ticks">
        <li><svg width="14" height="14" viewBox="0 0 16 16"><path d="M2 8l4 4 8-9" stroke="#2aa3df" stroke-width="2.5" fill="none"/></svg>Ut wisi enim ad minim veniam, quis nostrud exerci tation ullamcorper</li>
        <li><svg width="14" height="14" viewBox="0 0 16 16"><path d="M2 8l4 4 8-9" stroke="#2aa3df" stroke-width="2.5" fill="none"/></svg>Duis autem vel eum iriure dolor in hendrerit in vulputate velit esse molestie</li>
        <li><svg width="14" height="14" viewBox="0 0 16 16"><path d="M2 8l4 4 8-9" stroke="#2aa3df" stroke-width="2.5" fill="none"/></svg>ea nostrud exerci tation ullamcorper suscipit lobortis nisl ut aliquip</li>
        <li><svg width="14" height="14" viewBox="0 0 16 16"><path d="M2 8l4 4 8-9" stroke="#2aa3df" stroke-width="2.5" fill="none"/></svg>vel illum dolore eu feugiat nulla facilisis at vero eros et accumsan et iusto odio</li>
      </ul>
    </div>
    <div class="advantage-art" role="img" aria-label="Illustration of blue jigsaw puzzle pieces spelling public relations"></div>
  </div>
</section>

<section class="join">
  <div class="join-photo" role="img" aria-label="Photo of Asian business people in suits shaking hands"></div>
  <div class="join-body">
    <h2>JOIN US</h2>
    <p>Lorem ipsum dolor sit amet, consectetuer adipiscing elit, sed diam nonummy nibh euismod tincidunt ut laoreet dolore magna aliquam erat volutpat. Ut wisi enim ad minim veniam, quis nostrud exerci tation ullamcorper suscipit lobortis nisl ut aliquip ex ea commodo consequat.</p>
    <span class="btn"><svg width="16" height="14" viewBox="0 0 24 20" fill="#fff"><circle cx="9" cy="6" r="5"/><path d="M0 20c0-6 4-9 9-9s9 3 9 9z"/><path d="M20 4v8M16 8h8" stroke="#fff" stroke-width="2.5"/></svg>Join Us Now</span>
  </div>
</section>

<section class="partners">
  <span class="arrow">‹</span>
  <span class="partner">Northvale</span>
  <span class="partner">Kestrel</span>
  <span class="partner">Brightmoor</span>
  <span class="partner">Lumen Arc</span>
  <span class="partner">Tidewell</span>
  <span class="arrow">›</span>
</section>

<section class="news">
  <h2 class="section-title">COMPANY <span>NEWS</span></h2>
  <div class="title-rule"></div>
  <div class="wrap news-list">
    <article class="news-item">
      <div class="news-photo office" role="img" aria-label="Photo of an Asian businesswoman working at a laptop"></div>
      <div class="news-body">
        <h3>Lorem ipsum dolor sit a</h3>
        <div class="news-date"><i></i>Oct 07, 2014</div>
        <p>Sed diam nonummy nibh euismod tincidunt ut laoreet dolo aliquam erat volutpat. Ut wisi enim ad minim veniam, quis nostrud exerci tation ullamcorper suscipit lobortis nisl ut aliquip ex ea commodo consequat.</p>
        <span class="more">Read More ›</span>
      </div>
    </article>
    <article class="news-item">
      <div class="news-photo portrait" role="img" aria-label="Photo of an Asian businessman in a dark suit"></div>
      <div class="news-body">
        <h3>Lorem ipsum dolor sit a</h3>
        <div class="news-date"><i></i>Oct 07, 2014</div>
        <p>Sed diam nonummy nibh euismod tincidunt ut laoreet dolo aliquam erat volutpat. Ut wisi enim ad minim veniam, quis nostrud exerci tation ullamcorper suscipit lobortis nisl ut aliquip ex ea commodo consequat.</p>
        <span class="more">Read More ›</span>
      </div>
    </article>
  </div>
</section>

<footer class="site-footer">
  <div class="wrap">
    <div>
      <h5>QUICK LINKS</h5>
      <ul class="links">
        <li>› About Us</li><li>› Service Sector</li><li>› Professional Advantage</li><li>› Qianhai District</li><li>› Company News</li><li>› Join Us</li>
      </ul>
    </div>
    <div class="signup">
      <h5>NEWSLETTER SIGNUP</h5>
      <p>Lorem ipsum dolor sit amet, consectetuer adipiscing elit, sed diam nonummy nibh euismod.</p>
      <div class="field">Email Address</div>
      <span class="btn">SUBSCRIBE</span>
    </div>
    <div class="contact">
      <div class="contact-lines">
        <h5>CONTACT DETAIL</h5>
        <div><i></i><span>Unit 8 Harbourview Court,<br>Linden Row,<br>Qianhai Tower, 5180</span></div>
        <div><i></i><span>555-018-2046</span></div>
        <div><i></i><span>555-018-2047</span></div>
        <div><i></i><span>info@ovinpr.com</span></div>
      </div>
      <div class="map" role="img" aria-label="Street map showing the office location"></div>
    </div>
  </div>
</footer>

<div class="footer-bar">
  <div class="wrap">
    <span>Copyright © 2014 OVIN PR</span>
    <span class="follow">Follow Us : <i></i><i></i><i></i><i></i></span>
  </div>
</div>

</body>
</html>
```